IT Company: Big Data Product Brochure Design

DataLantern is a data management company developing next generation customer data technology. We're reworking an old brochure for our Big Data product called "KeenVue", which is a technology that gathers and matches social customer data to internal customer records for big companies. We've rewritten the text and are looking for a new design to go with it. We're looking for designs that suggest cutting-edge technology and sharp professionalism.
The brochure should be 8 1/2 x 11 inches, double sided. We will need both a print-quality PDF file and a small file size PDF to distribute digitally.
Industry/Entity Type
It Company
Look and feel

```html
<!DOCTYPE html>
<html lang="en">
<head>
<meta charset="utf-8">
<title>KeenVue – Platform Capabilities</title>
<link rel="stylesheet" href="https://fonts.googleapis.com/css2?family=Roboto+Condensed:ital,wght@0,400;0,700;1,400&display=swap">
<style>
  :root {
    --black: #0d0d0d;
    --charcoal: #2e2e2e;
    --green: #b5d334;
    --green-soft: #bcd94e;
    --page: #e8e8e8;
    --page-light: #f2f2f2;
    --row-light: #e6e6e6;
    --row-dark: #b1b2b4;
    --rule: #b9b9b9;
    --ink: #1a1a1a;
    --white: #ffffff;
  }
  * { box-sizing: border-box; margin: 0; padding: 0; }
  html, body { width: 927px; height: 1200px; overflow: hidden; }
  body {
    position: relative;
    font-family: "Roboto Condensed", "Arial Narrow", sans-serif;
    color: var(--ink);
    background: radial-gradient(ellipse at 50% 45%, var(--page-light) 0%, var(--page) 70%);
  }
  .masthead {
    position: absolute; left: 0; top: 0; width: 927px; height: 147px;
    background: linear-gradient(180deg, #3a3a3a 0%, var(--charcoal) 35%, var(--black) 100%);
  }
  .masthead-pointer { position: absolute; left: 432px; top: 146px; }
  .tagline {
    position: absolute; left: 27px; top: 24px;
    color: var(--white); font-weight: 700; font-size: 27px; line-height: 30px;
  }
  .tagline .hl { color: var(--green); }
  .power-line {
    position: absolute; right: 22px; top: 76px;
    display: flex; align-items: baseline; gap: 12px; color: var(--white);
  }
  .power-line .lead { font-size: 22px; font-weight: 700; }
  .product-name { font-size: 50px; font-weight: 700; color: var(--white); line-height: 1; }

  .section-title {
    position: absolute; left: 0; width: 927px; text-align: center;
    font-size: 32px; font-weight: 400; color: var(--ink);
  }
  .capabilities-title { top: 205px; }
  .applications-title { top: 564px; }

  .feature { position: absolute; top: 278px; }
  .feature-hub { left: 54px; }
  .feature-dashboard { left: 573px; }
  .feature h3 { font-size: 20px; font-weight: 700; margin-bottom: 6px; }
  .feature ul { list-style: none; padding-left: 14px; }
  .feature li { font-size: 15px; line-height: 30.5px; }
  .feature li::before { content: "•"; margin-right: 5px; }

  .divider {
    position: absolute; left: 79px; top: 528px; width: 770px; height: 2px;
    background: var(--rule);
  }

  .applications {
    position: absolute; left: 62px; top: 648px;
    display: grid;
    grid-template-columns: 116px repeat(4, 168px);
    column-gap: 2px; row-gap: 2px;
  }
  .applications .corner { background: transparent; }
  .applications .industry {
    height: 93px; background: var(--green-soft);
    display: flex; align-items: center; justify-content: center; text-align: center;
    font-size: 23px; line-height: 27px;
  }
  .applications .use {
    height: 33px; display: flex; align-items: center; justify-content: flex-end;
    font-size: 18px; padding-right: 10px; white-space: nowrap;
  }
  .applications .cell {
    height: 33px; display: flex; align-items: center; justify-content: center;
  }
  .row-light { background: var(--row-light); }
  .row-dark { background: var(--row-dark); }

  .maker-note {
    position: absolute; left: 24px; top: 1160px;
    font-size: 14px; font-style: italic;
  }
  .address-tab { position: absolute; left: 0; top: 1103px; }
  .address {
    position: absolute; right: 22px; top: 1118px; text-align: right;
    font-size: 15px; line-height: 18px;
  }
  .base-band { position: absolute; left: 0; top: 1188px; width: 927px; height: 12px; background: var(--green); }
</style>
</head>
<body>
  <svg width="0" height="0" style="position:absolute" aria-hidden="true">
    <defs>
      <symbol id="tick" viewBox="0 0 20 20">
        <path d="M2 11 L7 16 L18 3" fill="none" stroke="#111" stroke-width="2.6" stroke-linecap="round" stroke-linejoin="round"/>
      </symbol>
    </defs>
  </svg>

  <header class="masthead">
    <p class="tagline">Fore<span class="hl">sight</span>, hind<span class="hl">sight</span>, &amp; in<span class="hl">sight</span><br>combined...</p>
    <p class="power-line"><span class="lead">...that’s the power of</span><span class="product-name">KeenVue</span></p>
  </header>
  <svg class="masthead-pointer" width="62" height="32" viewBox="0 0 62 32" aria-hidden="true">
    <polygon points="0,0 62,0 31,32" fill="#0d0d0d"/>
  </svg>

  <h2 class="section-title capabilities-title">Platform Capabilities</h2>

  <section class="feature feature-hub">
    <h3>Big Data Hub</h3>
    <ul>
      <li>Centralize your Big Data into holistic records.</li>
      <li>Match and merge external data with your internal data.</li>
      <li>Measure the quality of your Big Data.</li>
      <li>Feed your Big Data into many analytical processes.</li>
      <li>Use your Big Data in real-time operational processes.</li>
      <li>Comply with privacy and security requirements.</li>
    </ul>
  </section>

  <section class="feature feature-dashboard">
    <h3>Big Data Governance Dashboard</h3>
    <ul>
      <li>Understand how your Big Data is changing.</li>
      <li>Visualize the quality of your Big Data.</li>
      <li>Report on metrics to support Data Governance.</li>
    </ul>
  </section>

  <div class="divider"></div>

  <h2 class="section-title applications-title">Industry Applications</h2>

  <div class="applications">
    <div class="corner"></div>
    <div class="industry">Retail</div>
    <div class="industry">Financial<br>Services</div>
    <div class="industry">Telecoms</div>
    <div class="industry">Travel</div>

    <div class="use">CRM</div>
    <div class="cell row-light"><svg width="20" height="20"><use href="#tick"/></svg></div>
    <div class="cell row-light"><svg width="20" height="20"><use href="#tick"/></svg></div>
    <div class="cell row-light"><svg width="20" height="20"><use href="#tick"/></svg></div>
    <div class="cell row-light"><svg width="20" height="20"><use href="#tick"/></svg></div>

    <div class="use">Loyalty</div>
    <div class="cell row-dark"><svg width="20" height="20"><use href="#tick"/></svg></div>
    <div class="cell row-dark"><svg width="20" height="20"><use href="#tick"/></svg></div>
    <div class="cell row-dark"><svg width="20" height="20"><use href="#tick"/></svg></div>
    <div class="cell row-dark"><svg width="20" height="20"><use href="#tick"/></svg></div>

    <div class="use">Fraud</div>
    <div class="cell row-light"></div>
    <div class="cell row-light"><svg width="20" height="20"><use href="#tick"/></svg></div>
    <div class="cell row-light"></div>
    <div class="cell row-light"></div>

    <div class="use">Marketing</div>
    <div class="cell row-dark"><svg width="20" height="20"><use href="#tick"/></svg></div>
    <div class="cell row-dark"><svg width="20" height="20"><use href="#tick"/></svg></div>
    <div class="cell row-dark"><svg width="20" height="20"><use href="#tick"/></svg></div>
    <div class="cell row-dark"><svg width="20" height="20"><use href="#tick"/></svg></div>

    <div class="use">Prospecting</div>
    <div class="cell row-light"><svg width="20" height="20"><use href="#tick"/></svg></div>
    <div class="cell row-light"><svg width="20" height="20"><use href="#tick"/></svg></div>
    <div class="cell row-light"><svg width="20" height="20"><use href="#tick"/></svg></div>
    <div class="cell row-light"><svg width="20" height="20"><use href="#tick"/></svg></div>

    <div class="use">Churn</div>
    <div class="cell row-dark"></div>
    <div class="cell row-dark"><svg width="20" height="20"><use href="#tick"/></svg></div>
    <div class="cell row-dark"><svg width="20" height="20"><use href="#tick"/></svg></div>
    <div class="cell row-dark"></div>
  </div>

  <svg class="address-tab" width="927" height="90" viewBox="0 0 927 90" aria-hidden="true">
    <polygon points="758,0 927,0 927,90 700,90" fill="#b5d334"/>
  </svg>
  <p class="address">48 Marlow Crescent, Ste 210<br>Kingsford K2R 4T7, Ontario<br>www.datalantern.com</p>
  <p class="maker-note">A DataLantern™ Product</p>
  <div class="base-band"></div>
</body>
</html>
```